Poster for a online company that buys your stuff

SwapHollow offers a website which customers can get a instant offer for stuff their looking to sell. They then Courier the items in to us and they get paid the same day it arrives
We're looking for an eye catching design which portrays our hassle free process
We'll need your help to come up with a slogan/catch phrase and our easy 1,2,3 process so customers can see the poster and instantly have a clear understanding of what we do
1. Get an instant offer on our website
2. Send your item(s) to us
3.Get paid within 24 Hours
Industry/Entity Type
It Company
Look and feel
Each slider illustrates characteristics of the customer's brand and the style your logo design should communicate.

```html
<!DOCTYPE html>
<html lang="en">
<head>
<meta charset="utf-8">
<title>SwapHollow – Selling has never been this easy</title>
<link rel="stylesheet" href="https://fonts.googleapis.com/css2?family=Fredoka:wght@600&family=Lato:wght@700;900&display=swap">
<style>
  :root {
    --backdrop: #dee1e5;
    --paper: #ffffff;
    --ink: #2b2b2b;
    --green: #9ccb3b;
    --green-deep: #7fae3d;
    --green-soft: #a9cf74;
    --yellow: #f0ce3c;
    --skin: #e6b89c;
    --skin-light: #f3d9c6;
    --hair: #6b4a36;
    --parcel: #f2a93b;
  }
  * { box-sizing: border-box; margin: 0; padding: 0; }
  html, body {
    width: 900px; height: 1200px; overflow: hidden;
    background: var(--backdrop);
    font-family: "Lato", Arial, sans-serif;
    color: var(--ink);
  }
  .poster {
    position: absolute; left: 94px; top: 222px;
    width: 712px; height: 595px;
    background: var(--paper);
    overflow: hidden;
  }
  .poster__band {
    position: absolute; left: 0; right: 0; top: 453px; bottom: 0;
    background: var(--yellow);
  }
  .mascot {
    position: absolute; left: 296px; top: 36px; width: 136px; height: 130px;
    border-radius: 40px;
    background:
      radial-gradient(ellipse 40% 35% at 72% 55%, var(--parcel) 0%, rgba(242,169,59,0) 100%),
      radial-gradient(ellipse 55% 60% at 45% 50%, var(--green) 0%, rgba(156,203,59,0.35) 60%, rgba(255,255,255,0) 100%);
  }
  .brand-name {
    position: absolute; left: 0; right: 0; top: 161px;
    text-align: center;
    font-weight: 900; font-size: 24px; letter-spacing: -0.3px;
    color: var(--ink);
  }
  .headline {
    position: absolute; left: 0; right: 0; top: 217px;
    text-align: center;
    font-family: "Fredoka", "Arial Rounded MT Bold", sans-serif;
    font-weight: 600; font-size: 26px; letter-spacing: 5.6px;
    color: var(--ink);
  }
  .headline__accent { color: var(--green); }
  .step-visual { position: absolute; top: 283px; height: 150px; }
  .step-visual--offer { left: 76px; width: 105px; }
  .step-visual--paid { left: 526px; width: 105px; }
  .step-visual--portrait {
    background:
      linear-gradient(90deg, rgba(255,255,255,1) 0%, rgba(255,255,255,0) 14%, rgba(255,255,255,0) 86%, rgba(255,255,255,1) 100%),
      linear-gradient(180deg, var(--hair) 0%, #8a634a 28%, var(--skin) 55%, var(--skin-light) 100%);
  }
  .step-visual--courier {
    left: 268px; top: 290px; width: 162px; height: 143px;
    background: linear-gradient(180deg, var(--green-soft) 0%, var(--green-deep) 100%);
    border-radius: 40px 40px 56px 56px;
    opacity: 0.95;
  }
  .step {
    position: absolute; top: 433px; width: 192px;
    text-align: center;
  }
  .step--1 { left: 35px; }
  .step--2 { left: 260px; }
  .step--3 { left: 485px; }
  .step__label {
    display: block; height: 42px; line-height: 42px;
    border-radius: 21px;
    background: var(--green); color: #fff;
    font-weight: 700; font-size: 14.5px;
  }
  .step__detail {
    display: block; margin-top: 2px;
    font-weight: 700; font-size: 14px;
  }
  .cta {
    position: absolute; left: 0; right: 0; top: 544px;
    text-align: center; font-weight: 700; font-size: 14px;
  }
</style>
</head>
<body>
  <main class="poster">
    <div class="poster__band"></div>

    <div class="mascot" role="img" aria-label="Cartoon courier mascot in a green cap giving a thumbs up while carrying an orange parcel"></div>
    <div class="brand-name">SwapHollow</div>

    <h1 class="headline">SELLING HAS NEVER BEEN <span class="headline__accent">THIS EASY</span></h1>

    <div class="step-visual step-visual--offer step-visual--portrait" role="img" aria-label="Step 1 photo: a woman with short brown hair looking surprised at an instant offer"></div>
    <div class="step-visual step-visual--courier" role="img" aria-label="Step 2 pictogram: green courier riding a delivery scooter with a parcel box on the back"></div>
    <div class="step-visual step-visual--paid step-visual--portrait" role="img" aria-label="Step 3 photo: the same woman grinning happily after getting paid"></div>

    <div class="step step--1">
      <span class="step__label">GET AN INSTANT OFFER</span>
      <span class="step__detail">on our website</span>
    </div>
    <div class="step step--2">
      <span class="step__label">SEND YOUR ITEM(S)</span>
      <span class="step__detail">to us via courier</span>
    </div>
    <div class="step step--3">
      <span class="step__label">GET PAID</span>
      <span class="step__detail">within 24 hours</span>
    </div>

    <p class="cta">Log on to www.swaphollow.co.nz</p>
  </main>
</body>
</html>
```